Fernvale Craft Works business card design- Fine Art sculpture business (Contract guaranteed)

This business card is for a fine art business. Though we don't have a website up and running yet it should be up soon. I would like the business card to be elegant and fairly simple with a picture of one of my sculptures on the front (you might need to photoshop out the background) as well as my basic contact info (my name,phone # and e-mail). On the back I'd like it to be pretty simple with just "Notes" and some blank lines for writing in info.

Target Market(s)

High end artwork buyers

Industry/Entity Type

Art Gallery

Contact Information for Business Card

Marlo Prewitt Phone: (555) 213-4098 E-mail: marlo@quillbrookmail.com Facebook: @fernvalecraftworks Instagram: fernvalecraftworks

Colors

Designer to choose colors to be used in the design.

Requirements
Must have
• *A picture of one of my sculptures*, my name, business name (Fernvale Craft Works), e-mail, phone #, and a notes section on the back.
• Fernvale Craft Works
• Marlo Prewitt
• (555)213-4098
• marlo@quillbrookmail.com
• Facebook: @fernvalecraftworks
• Instagram: fernvalecraftworks
Nice to have
• It'd be nice if you can crop out the background in the sculpture pictures, which ever one you end up using.

```html
<!DOCTYPE html>
<html lang="en">
<head>
<meta charset="utf-8">
<title>Fernvale Craft Works – Business Card</title>
<link rel="stylesheet" href="https://fonts.googleapis.com/css2?family=Kalam:wght@700&family=Roboto+Condensed:wght@400&display=swap">
<style>
  :root {
    --bg: #151515;
    --card: #ffffff;
    --purple: #6a3a9c;
    --ink: #2a2a2a;
    --halo: #eceaef;
    --amethyst: #6b34a8;
    --amethyst-deep: #3a2a78;
    --dots: #1e1e1e;
  }
  * { margin: 0; padding: 0; box-sizing: border-box; }
  html, body { width: 1200px; height: 799px; overflow: hidden; background: var(--bg); }
  .canvas { position: relative; width: 1200px; height: 799px; }

  .card {
    position: absolute; top: 50px; width: 400px; height: 700px;
    background: var(--card); overflow: hidden;
  }
  .card--back { left: 160px; }
  .card--front { left: 640px; }

  .photo {
    position: absolute;
    background: linear-gradient(160deg, var(--halo) 0%, var(--amethyst) 45%, var(--amethyst-deep) 100%);
  }
  .card--back .photo { left: 0; bottom: 0; width: 230px; height: 260px; border-top-right-radius: 120px; }
  .card--front .photo { left: 0; top: 95px; width: 200px; height: 605px; border-top-right-radius: 60px; }

  /* Front */
  .brand {
    position: absolute; top: 40px; right: 28px;
    font-family: "Kalam", cursive; font-weight: 700; font-size: 30px;
    color: var(--purple); line-height: 1;
  }
  .contact { position: absolute; top: 356px; left: 212px; }
  .contact__name {
    font-family: "Kalam", cursive; font-weight: 700; font-size: 25px;
    color: var(--purple); line-height: 1; margin-bottom: 8px;
  }
  .contact__line {
    display: flex; align-items: center; gap: 7px;
    font-family: "Roboto Condensed", sans-serif; font-size: 14px; color: var(--ink);
    line-height: 1.4;
  }
  .contact__icon { width: 14px; height: 12px; flex: none; }

  /* Back */
  .notes__title {
    position: absolute; top: 120px; left: 345px;
    font-family: "Kalam", cursive; font-weight: 700; font-size: 28px; color: var(--purple);
    line-height: 1; white-space: nowrap;
    transform: rotate(90deg); transform-origin: left top;
  }
  .notes__line {
    position: absolute; top: 80px; height: 400px; width: 0;
    border-left: 2px dotted var(--dots);
  }
</style>
</head>
<body>
<div class="canvas">

  <section class="card card--back">
    <div class="photo" role="img" aria-label="Photograph of an amethyst crystal sculpture"></div>
    <span class="notes__line" style="left:125px"></span>
    <span class="notes__line" style="left:200px"></span>
    <span class="notes__line" style="left:275px"></span>
    <h2 class="notes__title">Notes</h2>
  </section>

  <section class="card card--front">
    <div class="photo" role="img" aria-label="Photograph of an amethyst crystal arch sculpture on a stone base"></div>

    <h1 class="brand">Fernvale Craft Works</h1>

    <div class="contact">
      <p class="contact__name">Marlo Prewitt</p>
      <p class="contact__line">
        <svg class="contact__icon" viewBox="0 0 14 12" aria-hidden="true"><path d="M1 4 C1 1 13 1 13 4 L10 5 L9 3 L5 3 L4 5 Z M3 6 L11 6 L12 11 L2 11 Z" fill="var(--ink)"/></svg>
        (555)213-4098
      </p>
      <p class="contact__line">
        <svg class="contact__icon" viewBox="0 0 14 12" aria-hidden="true"><rect x="1" y="2" width="12" height="8" fill="none" stroke="var(--ink)" stroke-width="1.2"/><path d="M1 2 L7 7 L13 2" fill="none" stroke="var(--ink)" stroke-width="1.2"/></svg>
        marlo@quillbrookmail.com
      </p>
    </div>
  </section>

</div>
</body>
</html>
```